No Credit Score QT and ZMR

I'm looking for a banner to display on emails as well as facebook. The facebook banner would need to be square and the other size is 728 x 90. We are a mortgage company that does mostly Military home loans. We would like to start out with just this banner, then do about 20 others once we find the right designer. I need something simple but that stands out. Our company website is www.harborpeakfinancial.com. The text for this will be ( Ask about our "No Credit Score" program for ZMR and QT)

```html
<!DOCTYPE html>
<html lang="en">
<head>
<meta charset="utf-8">
<title>Harbor Peak Financial – No Credit Score Banner</title>
<link rel="stylesheet" href="https://fonts.googleapis.com/css2?family=Marcellus&display=swap">
<style>
  :root {
    --paper: #ffffff;
    --ink: #2a2a2a;
    --panel: #3b3b3b;
    --panel-text: #f4f4f4;
    --sky-light: #dfe7ee;
    --sky-mid: #b9c8d6;
    --roof: #6e6a66;
    --flag-red: #b3363a;
  }
  * { margin: 0; padding: 0; box-sizing: border-box; }
  html, body {
    width: 1200px;
    height: 148px;
    overflow: hidden;
    background: var(--paper);
  }
  .banner {
    position: relative;
    width: 1200px;
    height: 148px;
    background: var(--paper);
    overflow: hidden;
    font-family: "Marcellus", Georgia, serif;
  }
  .banner__shapes {
    position: absolute;
    inset: 0;
  }
  .brand {
    position: absolute;
    left: 30px;
    top: 36px;
    display: flex;
    align-items: center;
    gap: 16px;
    color: var(--ink);
  }
  .brand__square {
    width: 44px;
    height: 44px;
    background: var(--ink);
  }
  .brand__name {
    display: flex;
    flex-direction: column;
    line-height: 1;
  }
  .brand__primary {
    font-size: 38px;
    letter-spacing: 3px;
  }
  .brand__secondary {
    font-size: 15px;
    letter-spacing: 6px;
    margin-top: 6px;
    text-align: center;
  }
  .offer {
    position: absolute;
    left: 900px;
    right: 0;
    top: 0;
    height: 148px;
    display: flex;
    align-items: center;
    justify-content: center;
    text-align: center;
    color: var(--panel-text);
    font-size: 23px;
    line-height: 29px;
  }
</style>
</head>
<body>
  <div class="banner">
    <svg class="banner__shapes" width="1200" height="148" viewBox="0 0 1200 148" aria-hidden="false">
      <defs>
        <linearGradient id="homeTones" x1="0" y1="0" x2="1" y2="1">
          <stop offset="0" stop-color="var(--roof)"/>
          <stop offset="0.35" stop-color="var(--sky-mid)"/>
          <stop offset="0.6" stop-color="var(--sky-light)"/>
          <stop offset="0.8" stop-color="#c98a8c"/>
          <stop offset="1" stop-color="var(--sky-mid)"/>
        </linearGradient>
      </defs>
      <polygon role="img" aria-label="Photo of a house roofline with an American flag against a pale sky"
               points="478,0 920,0 880,148 432,148" fill="url(#homeTones)"/>
      <polygon class="offer-panel" points="898,0 1200,0 1200,148 857,148" fill="var(--panel)"/>
    </svg>

    <div class="brand">
      <span class="brand__square"></span>
      <span class="brand__name">
        <span class="brand__primary">HARBOR PEAK</span>
        <span class="brand__secondary">FINANCIAL, LLC</span>
      </span>
    </div>

    <p class="offer">Ask about our<br>"No Credit Score"<br>program for ZMR and QT</p>
  </div>
</body>
</html>
```